Building showcase catalogue for a post frame construction company

We are looking for a brochure for our clients showcasing our buildings. We are a post frame building company that makes commercial, ag, homes, and other building types. We are looking for a brochure that we can use with all the types of buildings simply by changing out the pictures. We would like a more photo heavy brochure thats 1-5 pages. We want the design to feel high end luxury. Our colors are black, white, and chrome. I will upload our logo as well as some building photos in the suburban category of our buildings. We would like a page to showcase some building layouts as well.

We need the size to be us letter size.

Industry/Entity Type

Construction

Font styles to use
Serif

Colors

Designer to choose only greyscale colors for use in the design.

Requirements
Must have
• A space to showcase building photos, small text space for information. An area to showcase building layouts.
Nice to have
• I would like to have a very clean professional look thats looks high end.
Should not have
• Areas for detail pictures. We mostly have exterior building shots.

```html
<!DOCTYPE html>
<html lang="en">
<head>
<meta charset="utf-8">
<title>Harwell Builders – Building Showcase Catalogue</title>
<link rel="stylesheet" href="https://fonts.googleapis.com/css2?family=Prata&family=Lora:wght@400;600&display=swap">
<style>
  :root{
    --backdrop:#dedede;
    --paper:#f4f4f4;
    --paper-shade:#e9e9e9;
    --ink:#0d1114;
    --ink-soft:#2e3439;
    --slate:#353c42;
    --chrome:#c9ccce;
    --white:#ffffff;
  }
  *{box-sizing:border-box;margin:0;padding:0}
  html,body{width:1200px;height:2520px;overflow:hidden;background:var(--backdrop)}
  body{position:relative;font-family:"Lora",Georgia,serif;color:var(--ink)}
  .spread{position:absolute;left:50px;width:1100px;height:712px;display:flex;box-shadow:0 18px 40px rgba(0,0,0,.18)}
  .spread--cover{top:64px}
  .spread--intro{top:904px}
  .spread--gallery{top:1744px}
  .page{position:relative;width:550px;height:712px;background:var(--paper);overflow:hidden}
  .page--left{background:linear-gradient(90deg,var(--paper) 85%,var(--paper-shade))}
  .page--right{background:linear-gradient(90deg,var(--paper-shade),var(--paper) 15%)}
  .page--dark{background:var(--ink)}
  .photo{position:absolute;display:block}
  .brand-name{font-family:"Lora",Georgia,serif;font-weight:600;letter-spacing:.08em;text-transform:uppercase;line-height:1.15}
  .headline{font-family:"Prata",Georgia,serif;font-weight:400;line-height:1.1}
  .body-copy{font-size:14px;line-height:1.3}
  .page-number{position:absolute;bottom:34px;font-size:14px;font-family:"Prata",Georgia,serif}

  /* cover spread */
  .back-photo{left:150px;top:110px;width:300px;height:170px;border-radius:60px 90px 50px 90px}
  .back-brand{position:absolute;left:60px;top:340px;font-size:17px;color:var(--ink)}
  .contact-list{position:absolute;left:250px;top:335px;list-style:none;font-size:14px;line-height:1.4}
  .contact-list li{display:flex;gap:6px;margin-bottom:8px;align-items:flex-start}
  .contact-list svg{flex:none;margin-top:3px}
  .cover-ring{position:absolute;left:130px;top:150px;width:380px;height:300px;border-radius:50%;border:6px solid var(--chrome);overflow:hidden}
  .cover-ring .photo{inset:0;width:100%;height:100%}
  .cover-brand{position:absolute;right:36px;top:70px;font-size:19px;color:var(--white);text-align:right}
  .cover-title{position:absolute;left:70px;top:470px;font-size:50px;color:var(--white)}
  .cover-sub{position:absolute;left:70px;top:540px;width:430px;font-size:14px;color:var(--chrome)}

  /* intro spread */
  .barn-photo{left:0;top:0;width:440px;height:250px}
  .annex-photo{left:430px;top:130px;width:240px;height:240px;z-index:2}
  .intro-title{position:absolute;left:100px;top:280px;font-size:44px;z-index:3}
  .intro-copy{position:absolute;left:100px;top:340px;width:310px}
  .rule-mark{position:absolute;left:70px;top:80px;right:40px;display:flex;align-items:center;gap:14px}
  .rule-mark .rule{flex:1;height:1px;background:var(--ink)}
  .rule-mark .brand-name{font-size:13px;color:var(--ink)}
  .feature-panel{position:absolute;left:140px;top:145px;width:380px;height:470px;background:linear-gradient(160deg,var(--slate),var(--ink));color:var(--white);padding:34px 34px}
  .feature-panel h2{font-size:25px;padding-bottom:12px;border-bottom:1px solid var(--chrome);margin-bottom:18px;font-weight:400}
  .feature-list{list-style:disc;padding-left:18px;font-size:13.5px;line-height:1.3}
  .feature-list li{margin-bottom:10px}
  .layout-plan{position:absolute;left:34px;right:34px;bottom:30px;height:120px}
  .layout-plan svg{width:100%;height:100%;display:block}
  .layout-caption{position:absolute;left:34px;bottom:156px;font-size:11px;letter-spacing:.12em;text-transform:uppercase;color:var(--chrome)}

  /* gallery spread */
  .gallery-title{position:absolute;left:230px;top:60px;font-size:42px}
  .gallery-copy{position:absolute;left:230px;top:115px;width:300px}
  .dark-band{position:absolute;left:0;top:200px;width:550px;height:230px;background:var(--ink)}
  .utility-photo{left:110px;top:245px;width:320px;height:220px;z-index:2}
  .kitchen-photo{left:-170px;top:190px;width:640px;height:430px;z-index:3}
</style>
</head>
<body>

<!-- Cover spread -->
<section class="spread spread--cover">
  <div class="page page--left">
    <svg class="photo back-photo" role="img" aria-label="Exterior photo of a white board-and-batten home with timber gable entry" viewBox="0 0 300 170" preserveAspectRatio="none">
      <defs><linearGradient id="backGrad" x1="0" y1="0" x2="0" y2="1"><stop offset="0" stop-color="#cfd6dc"/><stop offset=".6" stop-color="#e6e6e4"/><stop offset="1" stop-color="#8a8580"/></linearGradient></defs>
      <rect width="300" height="170" fill="url(#backGrad)"/>
    </svg>
    <p class="brand-name back-brand">Harwell<br>Builders, Inc.</p>
    <ul class="contact-list">
      <li><svg width="12" height="12" viewBox="0 0 24 24"><path fill="currentColor" d="M6.6 10.8a15 15 0 006.6 6.6l2.2-2.2a1 1 0 011-.25 11.4 11.4 0 003.6.6 1 1 0 011 1V20a1 1 0 01-1 1A17 17 0 013 4a1 1 0 011-1h3.5a1 1 0 011 1c0 1.250.2 2.450.6 3.6a1 1 0 01-.25 1z"/></svg>(+012) 234 -567</li>
      <li><svg width="12" height="12" viewBox="0 0 24 24"><path fill="currentColor" d="M2 5h20v14H2zm2 2v.5l8 5 8-5V7z"/></svg>info@yourmail.com</li>
      <li><svg width="12" height="12" viewBox="0 0 24 24"><path fill="currentColor" d="M12 2a7 7 0 00-7 7c0 5 7 13 7 13s7-8 7-13a7 7 0 00-7-7zm0 9.5A2.5 2.5 0 1112 6.5a2.5 2.5 0 010 5z"/></svg><span>123, Lorem ipsum dolor sit<br>amet, cons 9867<br>ectetur Adipiscing</span></li>
    </ul>
  </div>
  <div class="page page--dark">
    <p class="brand-name cover-brand">Harwell<br>Builders, Inc.</p>
    <div class="cover-ring">
      <svg class="photo" role="img" aria-label="Interior photo of a warm timber-ceiling living room with leather sofas and pendant lights" viewBox="0 0 100 100" preserveAspectRatio="none">
        <defs><linearGradient id="coverGrad" x1="0" y1="0" x2="0" y2="1"><stop offset="0" stop-color="#a8663a"/><stop offset=".5" stop-color="#6b3a28"/><stop offset="1" stop-color="#4a3630"/></linearGradient></defs>
        <rect width="100" height="100" fill="url(#coverGrad)"/>
      </svg>
    </div>
    <h1 class="headline cover-title">Lorem ipsum</h1>
    <p class="cover-sub">Quis autem vel eum iure reprehenderit qui in ea voluptate ve lit esse quam nihil molestiae consequatur</p>
  </div>
</section>

<!-- Intro spread -->
<section class="spread spread--intro">
  <div class="page page--left" style="overflow:visible">
    <svg class="photo barn-photo" role="img" aria-label="Exterior photo of a red post frame home with landscaped stone garden" viewBox="0 0 100 100" preserveAspectRatio="none">
      <defs><linearGradient id="barnGrad" x1="0" y1="0" x2="0" y2="1"><stop offset="0" stop-color="#b9c6d2"/><stop offset=".35" stop-color="#8e2a2c"/><stop offset=".75" stop-color="#6a2426"/><stop offset="1" stop-color="#9b8f7c"/></linearGradient></defs>
      <rect width="100" height="100" fill="url(#barnGrad)"/>
    </svg>
    <svg class="photo annex-photo" role="img" aria-label="Exterior photo of a red post frame garage with gravel drive" viewBox="0 0 100 100" preserveAspectRatio="none">
      <defs><linearGradient id="annexGrad" x1="0" y1="0" x2="0" y2="1"><stop offset="0" stop-color="#8fb3d6"/><stop offset=".4" stop-color="#9a3032"/><stop offset=".7" stop-color="#7d2b2c"/><stop offset="1" stop-color="#b4aa98"/></linearGradient></defs>
      <rect width="100" height="100" fill="url(#annexGrad)"/>
    </svg>
    <h2 class="headline intro-title">Lorem ipsum</h2>
    <p class="body-copy intro-copy">Lorem ipsum dolor sit amet, consectetur adipisci ng elit, sed do eiusmod tempor incididunt ut labore et dolore magna aliqua. Ut enim ad minim veniam, quis nostrud exercitation ullamco laboris nisi ut aliquip ex</p>
    <span class="page-number" style="left:70px">01</span>
  </div>
  <div class="page page--right">
    <div class="rule-mark"><span class="rule"></span><span class="brand-name">Harwell</span></div>
    <div class="feature-panel">
      <h2 class="headline">Quis autem vel eum iure reprehen</h2>
      <ul class="feature-list">
        <li>Lorem ipsum dolor sit amet, con sectetur adipiscing</li>
        <li>Elit, sed do eiusmod tempor incid idunt ut labore et dolore</li>
        <li>Magna aliqua. Ut enim ad minim veniam, quis nostrud</li>
        <li>Exercitation ullamco laboris nisi ut aliquip ex</li>
      </ul>
      <p class="layout-caption">Building layout</p>
      <div class="layout-plan">
        <svg viewBox="0 0 312 120" role="img" aria-label="Building floor plan layout area">
          <g fill="none" stroke="#c9ccce" stroke-width="1.5">
            <rect x="1" y="1" width="310" height="118"/>
            <line x1="120" y1="1" x2="120" y2="119"/>
            <line x1="120" y1="60" x2="311" y2="60"/>
            <line x1="220" y1="60" x2="220" y2="119"/>
          </g>
        </svg>
      </div>
    </div>
    <span class="page-number" style="right:70px">02</span>
  </div>
</section>

<!-- Gallery spread -->
<section class="spread spread--gallery">
  <div class="page page--left">
    <h2 class="headline gallery-title">Lorem ipsum</h2>
    <p class="body-copy gallery-copy">Lorem ipsum dolor sit amet, consectetur adipisci ng elit, sed do eiusmod tempor incididunt ut labore et dolore magna aliqua.</p>
    <div class="dark-band"></div>
    <svg class="photo utility-photo" role="img" aria-label="Photo of a utility vehicle parked inside a steel-lined building" viewBox="0 0 100 100" preserveAspectRatio="none">
      <defs><linearGradient id="utilGrad" x1="0" y1="0" x2="0" y2="1"><stop offset="0" stop-color="#a9aaa5"/><stop offset=".6" stop-color="#5a5552"/><stop offset="1" stop-color="#7d766f"/></linearGradient></defs>
      <rect width="100" height="100" fill="url(#utilGrad)"/>
    </svg>
    <span class="page-number" style="left:70px">03</span>
  </div>
  <div class="page page--right" style="overflow:visible">
    <div class="rule-mark"><span class="rule"></span><span class="brand-name">Harwell</span></div>
    <svg class="photo kitchen-photo" role="img" aria-label="Interior photo of a kitchen with whitewashed wood cabinets and stainless fridge" viewBox="0 0 100 100" preserveAspectRatio="none">
      <defs><linearGradient id="kitGrad" x1="0" y1="0" x2="1" y2="1"><stop offset="0" stop-color="#b8b3a8"/><stop offset=".5" stop-color="#cfc6b6"/><stop offset="1" stop-color="#6f6256"/></linearGradient></defs>
      <rect width="100" height="100" fill="url(#kitGrad)"/>
    </svg>
    <span class="page-number" style="right:70px">04</span>
  </div>
</section>

</body>
</html>
```